Counseling Practice Business Card

I need a professional looking business card incorporating my new logo that was just completed. Card needs to incorporate my name and title, description of my specialty, my address, my phone number, my fax number, my email and my website URL. I need to be able to choose design on/with different paper colors and textures.
I do not have a lot of business card ideas so I am open to anything but I want bold,sharp, clear card without additional designs other than my logo (see attached file info). I am open to different color backgrounds or paper colors including black. I do not like traditional brackets around area codes in phone number or dashes between numbers in phone number. Am open to other ways of presenting including periods between numbers as appropriate. I do not know enough to know what I like yet but I want card to coordinate and work together with my logo. My practice emphasizes natural mental health interventions so any use of color (with background paper color or the blue and green in my logo) that elicits nature is nice. In addition to black, any natural brown or wood looking background might be desirable also. Most of the offerings so far look very similar and boring.

Target Market(s)

Potential therapy clients and other professionals

Contact Information for Business Card

Card information:
Marcus T. Whitfield, Ph.D.
Licensed Clinical Psychologist
Integrative Health Coach
4812 Ferndale Pkwy NW
Suite 730
Duluth, GA 30096
(770) 555-0142 phone
(770) 555-0186 fax
drmarcuswhitfield@kelvora.com
pathbloomcounseling.com

Font styles to use
Serif
Sans Serif
Other font styles liked:
• anything that you think looks crisp, clear and easily readable

Requirements
Must have
• Any color used should coordinate with my logo design (see attached files).
• Card should be printed horizontally so top and bottom are longest sides of rectangle.
• Background color or paper color should complement and highlight logo. Do not like a white background. black, grey, brown or any color my logo would blend well with.
Nice to have
• I would like designer to utilize color to highlight letters/name or phone-fax-web symbols.
• Bottom edge of card could be highlighted if appropriate to an idea.
Should not have
• I would NOT want the card to have a pure white background at all.
• No clear cards.
• Cards should be oriented with long sides on bottom and top, NOT sides. DO NOT LIKE THIS THIN TALL ORIENTATION.

```html
<!DOCTYPE html>
<html lang="en">
<head>
<meta charset="utf-8">
<title>Pathbloom Counseling – Business Card Versions</title>
<link rel="stylesheet" href="https://fonts.googleapis.com/css2?family=Montserrat:wght@300;400;600;700;800&display=swap">
<style>
  :root {
    --board: #4a4b4d;
    --label: #7b7c7e;
    --white: #ffffff;
    --paper-light: #e6e6e6;
    --paper-dark: #2b2b2c;
    --ink-dark: #2a2a2b;
    --ink-light: #e8e8e8;
    --green: #116b32;
    --blue: #2a72b8;
    --bar-dark: #353536;
    --bar-on-dark: #3f3f41;
    --plastic-top: #a9aaab;
    --plastic-bottom: #8d8e90;
  }
  * { margin: 0; padding: 0; box-sizing: border-box; }
  html, body { width: 1200px; height: 1200px; overflow: hidden; }
  body {
    position: relative;
    background: var(--board);
    font-family: "Montserrat", sans-serif;
  }

  .version-label {
    position: absolute;
    right: 878px;
    text-align: right;
    color: var(--label);
  }
  .version-label .number { display: block; font-size: 52px; font-weight: 800; line-height: 1; letter-spacing: -1px; }
  .version-label .name { display: block; font-size: 27px; font-weight: 400; letter-spacing: 1px; line-height: 1.1; }

  .card {
    position: absolute;
    left: 354px;
    width: 492px;
    height: 282px;
    border-radius: 7px;
    overflow: hidden;
    box-shadow: 0 6px 14px rgba(0,0,0,0.35);
  }
  .card--light { top: 106px; background: var(--paper-light); color: var(--ink-dark); }
  .card--dark { top: 433px; background: var(--paper-dark); color: var(--ink-light); }
  .card--plastic {
    top: 757px; left: 350px; width: 500px; height: 288px; border-radius: 12px;
    background: linear-gradient(180deg, var(--plastic-top), var(--plastic-bottom));
    color: #f1f1f1;
    border: 2px solid rgba(255,255,255,0.35);
  }

  .edge { position: absolute; left: 0; right: 0; height: 10px; display: flex; }
  .edge--top { top: 0; }
  .edge--bottom { bottom: 0; }
  .edge span { display: block; height: 100%; }
  .edge--top .green { width: 290px; background: var(--green); }
  .edge--top .blue { flex: 1; background: var(--blue); }
  .edge--bottom .blue { width: 202px; background: var(--blue); }
  .edge--bottom .green { flex: 1; background: var(--green); }

  .holder { position: absolute; left: 32px; }
  .holder .full-name { font-size: 17.5px; font-weight: 700; letter-spacing: -0.3px; white-space: nowrap; }
  .holder .full-name .degree { font-weight: 300; }
  .holder .specialty {
    display: inline-block; margin-top: 3px; padding: 2px 6px;
    font-size: 10.5px; font-weight: 400; white-space: nowrap;
  }
  .card--light .specialty { background: var(--bar-dark); color: var(--white); }
  .card--dark .specialty { background: var(--bar-on-dark); color: var(--ink-light); }
  .card--plastic .specialty { padding-left: 5px; }

  .contact { position: absolute; left: 32px; list-style: none; font-size: 11.5px; font-weight: 400; letter-spacing: 0.6px; }
  .contact li { line-height: 17px; }

  .brand {
    position: absolute; left: 362px; display: flex; align-items: center; gap: 5px;
    font-size: 19px; font-weight: 600; color: var(--blue); letter-spacing: -0.3px;
  }
  .brand .dot { width: 10px; height: 10px; border-radius: 50%; background: var(--green); }
  .card--plastic .brand { left: 366px; }

  .rule { position: absolute; left: 32px; width: 430px; height: 1.5px; background: var(--blue); }
  .address { position: absolute; left: 32px; font-size: 11px; font-weight: 400; letter-spacing: 2.6px; white-space: nowrap; }

  .swatches { position: absolute; top: 1094px; left: 478px; display: flex; gap: 14px; }
  .swatches span { width: 38px; height: 38px; display: block; }

  .board-caption {
    position: absolute; top: 1149px; left: 0; width: 1200px; text-align: center;
    font-size: 18px; font-weight: 700; color: var(--label); letter-spacing: 0.4px;
  }
</style>
</head>
<body>

  <div class="version-label" style="top:212px"><span class="number">01</span><span class="name">LIGHT VERSION</span></div>
  <div class="version-label" style="top:538px"><span class="number">02</span><span class="name">DARK VERSION</span></div>
  <div class="version-label" style="top:861px"><span class="number">03</span><span class="name">ON PLASTIC</span></div>

  <article class="card card--light">
    <div class="edge edge--top"><span class="green"></span><span class="blue"></span></div>
    <div class="holder" style="top:40px">
      <div class="full-name">MARCUS T. WHITFIELD, <span class="degree">PH.D</span></div>
      <div class="specialty">LICENSED CLINICAL PSYCHOLOGIST / INTEGRATIVE HEALTH COACH</div>
    </div>
    <ul class="contact" style="top:148px">
      <li>(770) 555-0142</li>
      <li>(770) 555-0186</li>
      <li>drmarcuswhitfield@kelvora.com</li>
      <li>www.pathbloomcounseling.com</li>
    </ul>
    <div class="brand" style="top:185px"><span class="dot"></span>Pathbloom</div>
    <div class="rule" style="top:227px"></div>
    <div class="address" style="top:235px">4812 Ferndale Pkwy NW, Suite 730, Duluth, GA 30096</div>
    <div class="edge edge--bottom"><span class="blue"></span><span class="green"></span></div>
  </article>

  <article class="card card--dark">
    <div class="edge edge--top"><span class="green"></span><span class="blue"></span></div>
    <div class="holder" style="top:90px">
      <div class="full-name">MARCUS T. WHITFIELD, <span class="degree">PH.D</span></div>
      <div class="specialty">LICENSED CLINICAL PSYCHOLOGIST / INTEGRATIVE HEALTH COACH</div>
    </div>
    <ul class="contact" style="top:146px">
      <li>(770) 555-0142</li>
      <li>(770) 555-0186</li>
      <li>drmarcuswhitfield@kelvora.com</li>
      <li>www.pathbloomcounseling.com</li>
    </ul>
    <div class="brand" style="top:183px"><span class="dot"></span>Pathbloom</div>
    <div class="rule" style="top:226px"></div>
    <div class="address" style="top:234px">4812 Ferndale Pkwy NW, Suite 730, Duluth, GA 30096</div>
    <div class="edge edge--bottom"><span class="blue"></span><span class="green"></span></div>
  </article>

  <article class="card card--plastic">
    <div class="holder" style="top:47px">
      <div class="full-name">MARCUS T. WHITFIELD, <span class="degree">PH.D</span></div>
      <div class="specialty">LICENSED CLINICAL PSYCHOLOGIST / INTEGRATIVE HEALTH COACH</div>
    </div>
    <ul class="contact" style="top:157px">
      <li>(770) 555-0142</li>
      <li>(770) 555-0186</li>
      <li>drmarcuswhitfield@kelvora.com</li>
      <li>www.pathbloomcounseling.com</li>
    </ul>
    <div class="brand" style="top:195px"><span class="dot"></span>Pathbloom</div>
    <div class="rule" style="top:238px"></div>
    <div class="address" style="top:246px">4812 Ferndale Pkwy NW, Suite 730, Duluth, GA</div>
  </article>

  <div class="swatches">
    <span style="background:var(--white)"></span>
    <span style="background:var(--paper-light)"></span>
    <span style="background:var(--bar-on-dark)"></span>
    <span style="background:var(--green)"></span>
    <span style="background:var(--blue)"></span>
  </div>

  <div class="board-caption">BUSINESS CARD DESIGN MOCKUPS 01 FOR PATHBLOOM COUNSELING</div>

</body>
</html>
```